Luxury Business Card Design for High-End Window Treatments

Gilded Vantages
Custom Plantation Shutters & Architectural Shading Systems

⸻

BACK

Daniel Forsythe
Owner

Custom Interior & Exterior Window Treatments

919-482-7034
gildedvantages.com

I have included a picture that I’m hoping we can use on the back, but I’m also wondering if you can get rid of the ladder? Should we get rid of shutters , shades and blinds underneath Gilded Vantages?

Target Market(s)

High-end residential homeowners, custom home builders, architects, interior designers, and luxury renovation clients seeking premium plantation shutters and motorized architectural shading systems.

Industry/Entity Type

Custom Window treatments

Contact Information for Business Card

Front Gilded Vantages Custom Plantation Shutters Motorized Architectural Shading Systems BACK Daniel Forsythe Owner 919-482-7034 GildedVantages.com Custom Interior & Exterior Window Treatments By Appointment

Requirements
Nice to have
• Not 100% sure on nice to halves or the color but you can definitely check out my website to get a better understanding of what I’m trying to do

```html
<!DOCTYPE html>
<html lang="en">
<head>
<meta charset="utf-8">
<title>Gilded Vantages – Business Card</title>
<link rel="stylesheet" href="https://fonts.googleapis.com/css2?family=Quattrocento:wght@400;700&family=Quattrocento+Sans&display=swap">
<style>
  :root {
    --backdrop: #6a6a6c;
    --card: #1e1e1f;
    --gold: #f3d968;
    --band: #fce36a;
    --ink-light: #e6e2da;
    --ink-dark: #141414;
    --front-mark: #5a5a5a;
    --divider: #d8d4cc;
  }
  * { margin: 0; padding: 0; box-sizing: border-box; }
  html, body { width: 900px; height: 1200px; overflow: hidden; }
  body { background: var(--backdrop); position: relative; font-family: "Quattrocento", serif; }

  .card {
    position: absolute;
    left: 135px;
    width: 630px;
    height: 358px;
    background: var(--card);
    overflow: hidden;
  }
  .card--front { top: 214px; }
  .card--back { top: 628px; }

  .brand-name {
    position: absolute;
    font-family: "Quattrocento Sans", sans-serif;
    font-weight: 400;
    line-height: 1;
    text-align: center;
  }
  .brand-name span { display: block; }
  .card--front .brand-name {
    left: 169px; width: 294px; top: 94px;
    font-size: 62px; color: var(--front-mark);
  }
  .card--back .brand-name {
    left: 40px; width: 276px; top: 100px;
    font-size: 54px; color: var(--ink-light);
  }

  .services {
    position: absolute;
    font-family: "Quattrocento Sans", sans-serif;
    color: var(--gold);
    display: flex;
    justify-content: space-between;
  }
  .card--front .services { left: 168px; width: 297px; top: 250px; font-size: 25px; }
  .card--back .services { left: 52px; width: 254px; top: 241px; font-size: 22px; }

  .divider {
    position: absolute;
    left: 332px; top: 77px;
    width: 2px; height: 206px;
    background: var(--divider);
  }

  .contact { position: absolute; left: 357px; top: 72px; color: var(--ink-light); }
  .contact__name { font-size: 25px; color: var(--gold); line-height: 1.1; }
  .contact__role { font-size: 15px; letter-spacing: 1.5px; margin-top: 5px; }
  .contact__rule { width: 48px; height: 2px; background: var(--gold); margin-top: 6px; }
  .contact__address { font-size: 15px; letter-spacing: 0.8px; line-height: 25px; margin-top: 10px; }
  .contact__line { display: flex; align-items: center; gap: 6px; font-size: 15px; letter-spacing: 0.8px; height: 24px; }
  .contact__line--phone { letter-spacing: 4px; margin-top: 3px; }
  .contact__line svg { width: 12px; height: 12px; fill: var(--gold); flex: none; }

  .appointment-band {
    position: absolute;
    left: 0; top: 305px;
    width: 630px; height: 30px;
    background: var(--band);
    color: var(--ink-dark);
    font-weight: 700;
    font-size: 17px;
    text-align: center;
    line-height: 30px;
  }
</style>
</head>
<body>

<section class="card card--front" aria-label="Card front">
  <h1 class="brand-name"><span>Gilded</span><span>Vantages</span></h1>
  <p class="services"><span>Shutters</span><span>Shades</span><span>Blinds</span></p>
</section>

<section class="card card--back" aria-label="Card back">
  <h2 class="brand-name"><span>Gilded</span><span>Vantages</span></h2>
  <p class="services"><span>Shutters</span><span>Shades</span><span>Blinds</span></p>

  <div class="divider"></div>

  <div class="contact">
    <p class="contact__name">Daniel Forsythe</p>
    <p class="contact__role">Owner</p>
    <div class="contact__rule"></div>
    <p class="contact__address">418 Alder Row<br>Suite 210 #3307<br>Linwood, NC 28190</p>
    <p class="contact__line contact__line--phone">
      <svg viewBox="0 0 24 24" aria-hidden="true"><path d="M6.6 10.8a15.1 15.1 0 0 0 6.6 6.6l2.2-2.2a1 1 0 0 1 1-.25 11.4 11.4 0 0 0 3.6.57 1 1 0 0 1 1 1V20a1 1 0 0 1-1 1A17 17 0 0 1 3 4a1 1 0 0 1 1-1h3.5a1 1 0 0 1 1 1c0 1.25.2 2.45.57 3.57a1 1 0 0 1-.25 1z"/></svg>
      919-482-7034
    </p>
    <p class="contact__line">
      <svg viewBox="0 0 24 24" aria-hidden="true"><path d="M2 5h20v14H2z M2 5l10 8 10-8" fill="var(--gold)"/><path d="M2 6l10 7.5L22 6" fill="none" stroke="var(--card)" stroke-width="1.8"/></svg>
      info@gildedvantages.com
    </p>
    <p class="contact__line">
      <svg viewBox="0 0 24 24" aria-hidden="true"><circle cx="12" cy="12" r="9.5" fill="none" stroke="var(--gold)" stroke-width="2"/><path d="M2.5 12h19M12 2.5v19M5 7h14M5 17h14" fill="none" stroke="var(--gold)" stroke-width="1.5"/><ellipse cx="12" cy="12" rx="4.5" ry="9.5" fill="none" stroke="var(--gold)" stroke-width="1.5"/></svg>
      gildedvantages.com
    </p>
  </div>

  <p class="appointment-band">Custom Interior &amp; Exterior Window Treatments By Appointment</p>
</section>

</body>
</html>
```